Design a standard roll up banner

Hello Contestant! We are looking for a standard roll up banner for our Financial Planning Practice.

We are specialized on the niche market of the FRENCH executives and entrepreneurs living in the United States. We are working with them, so they can be prepared at best to the American retirement, protection, fiscal and saving system.

We would like someone to make a roll up banner that that fit with the theme of our website and logo colors (link below) with the theme France & USA.

Website link: http://www.brightmorrowwealth.com

In the banner we want to include

Our name : Brightmorrow Wealth Partners

Our activity : Gestion Privée aux Etats-Unis

Our Tag line: Ensemble capitalisons votre réussite et construisons votre patrimoine aux Etats-Unis.

The list of our services:
 Stratégie patrimoniale internationale
 Placements financiers
 Assurance et gestion des risques
 Optimisation couverture salariale

The list of cities we are working in:

New York – San Francisco – Miami – Philadelphia – Los Angeles – San Diego – Houston – Detroit – Chicago – Boston – Washington D.C. – Seattle – Atlanta

Banner Specifications:
- Dimensions I 47-inch width, 81-inch height I 120cm width, 205cm height I
- Blue, red and white colors preferred
- Formal, modern design

I have attache our old banner as well as our logo

```html
<!DOCTYPE html>
<html lang="fr">
<head>
<meta charset="utf-8">
<title>Brightmorrow Wealth Partners – Roll-up</title>
<link rel="stylesheet" href="https://fonts.googleapis.com/css2?family=Lato:wght@400;700;900&display=swap">
<style>
  :root {
    --page: #e9ebef;
    --navy: #131a33;
    --navy-deep: #0d1328;
    --navy-soft: #1f2a4d;
    --blue: #1f4fb5;
    --blue-bright: #2f6fd6;
    --red: #e0202f;
    --white: #ffffff;
    --text-soft: #d9deea;
  }
  * { box-sizing: border-box; margin: 0; padding: 0; }
  html, body { width: 1200px; height: 899px; overflow: hidden; }
  body {
    background: var(--page);
    font-family: "Lato", Arial, sans-serif;
    position: relative;
  }
  .banner {
    position: absolute;
    left: 419px; top: 18px;
    width: 362px; height: 864px;
    background: var(--navy);
    overflow: hidden;
    box-shadow: 0 6px 24px rgba(0,0,0,.18);
  }
  .top-strip { position: absolute; left: 0; top: 0; width: 100%; height: 51px; background: var(--navy-deep); }
  .top-strip .tab { position: absolute; left: 122px; top: 0; width: 122px; height: 51px; background: var(--navy-soft); }
  .top-rule { position: absolute; left: 0; top: 51px; width: 100%; height: 5px; background: var(--blue); }
  .hero { position: absolute; left: 0; top: 56px; width: 362px; height: 227px; }
  .hero svg { display: block; }
  .brand-seal {
    position: absolute;
    width: 88px; height: 88px; border-radius: 50%;
    background: var(--white);
    display: flex; align-items: center; justify-content: center;
    text-align: center;
    color: var(--navy);
    font-weight: 700; font-size: 10px; line-height: 1.15;
    padding: 8px;
  }
  .brand-seal.top { left: 5px; top: 70px; }
  .brand-seal.bottom { left: 137px; top: 701px; }
  .activity {
    position: absolute; left: 24px; top: 305px;
    color: var(--blue-bright);
    font-weight: 900; font-size: 20px; line-height: 1.05;
    text-transform: uppercase;
  }
  .tagline {
    position: absolute; left: 24px; top: 366px; width: 320px;
    color: var(--white);
    font-size: 14px; line-height: 1.4;
  }
  .section-title {
    position: absolute; left: 24px;
    color: var(--white);
    font-weight: 900; font-size: 22px; line-height: 26px;
    text-transform: uppercase;
  }
  .section-title.services { top: 415px; }
  .section-title.cities-title { top: 575px; }
  .services-list {
    position: absolute; left: 14px; top: 455px;
    list-style: none;
    color: var(--text-soft);
    font-size: 16.5px; line-height: 24px;
  }
  .services-list li { display: flex; align-items: center; height: 24px; }
  .services-list li::before {
    content: ""; flex: none; width: 12px; height: 12px; margin-right: 14px;
    background: var(--red); border: 3px solid var(--white); border-radius: 2px;
    box-shadow: 0 0 0 1px var(--red);
  }
  .cities {
    position: absolute; left: 14px; top: 609px; width: 334px;
    color: var(--text-soft);
    font-size: 11.5px; line-height: 17.5px; text-align: center;
  }
  .chevron { position: absolute; left: 0; top: 685px; }
  .footer-band { position: absolute; left: 0; top: 792px; width: 100%; height: 28px; background: var(--navy-deep); }
  .footer-url {
    position: absolute; left: 0; top: 820px; width: 100%; height: 44px;
    background: var(--navy);
    color: var(--text-soft); font-size: 13px;
    display: flex; align-items: center; justify-content: center;
  }
</style>
</head>
<body>
  <section class="banner">
    <div class="top-strip"><div class="tab"></div></div>
    <div class="top-rule"></div>

    <div class="hero">
      <svg width="362" height="227" viewBox="0 0 362 227">
        <defs>
          <linearGradient id="skyline" x1="0" y1="0" x2="0" y2="1">
            <stop offset="0" stop-color="#8d9bab"/>
            <stop offset="0.45" stop-color="#c9b596"/>
            <stop offset="0.75" stop-color="#5a5a62"/>
            <stop offset="1" stop-color="#2a2d36"/>
          </linearGradient>
        </defs>
        <rect width="362" height="227" fill="url(#skyline)" role="img" aria-label="New York skyline at sunset"/>
        <polygon points="296,0 362,0 362,76" fill="var(--white)"/>
        <polygon points="306,0 362,0 362,62" fill="var(--blue)"/>
        <polygon points="0,227 0,165 216,195 362,170 362,227" fill="var(--white)"/>
        <polygon points="0,227 0,172 216,202 362,178 362,227" fill="var(--red)"/>
        <polygon points="0,227 0,212 216,222 362,207 362,227" fill="var(--navy)"/>
      </svg>
    </div>
    <div class="brand-seal top">Brightmorrow Wealth Partners</div>

    <h1 class="activity">Gestion privée<br>aux Etats-Unis</h1>
    <p class="tagline">Ensemble capitalisons votre réussite et construisons votre patrimoine aux Etats-Unis.</p>

    <h2 class="section-title services">Our services:</h2>
    <ul class="services-list">
      <li>Stratégie patrimoniale internationale</li>
      <li>Placements financiers</li>
      <li>Assurance et gestion des risques</li>
      <li>Optimisation couverture salariale</li>
    </ul>

    <h2 class="section-title cities-title">We are working in:</h2>
    <p class="cities">New York – San Francisco – Miami – Philadelphia – Los Angeles – San Diego – Houston – Detroit – Chicago – Boston – Washington D.C. – Seattle – Atlanta</p>

    <svg class="chevron" width="362" height="107" viewBox="0 0 362 107">
      <polygon points="0,42 181,0 362,42 362,107 0,107" fill="var(--blue)"/>
      <polyline points="0,42 181,0 362,42" fill="none" stroke="var(--blue-bright)" stroke-width="3"/>
    </svg>
    <div class="brand-seal bottom">Brightmorrow Wealth Partners</div>

    <div class="footer-band"></div>
    <div class="footer-url">http://www.brightmorrowwealth.com</div>
  </section>
</body>
</html>
```